Chiropractic healthcare group business card

We are a Portland Oregon based chiropractic healthcare group. Looking for a new business card design. Something cutting edge, that shows off our new logo and tag line.Use either of the attached logos.Our tag line = "Who would you be without pain?"I'm open to about anything, impress me!!
Target Market(s)
Chiropractic patients - Auto injury, back pain, sports injuries, neck , shoulder, hip, knee, ankle pain.
Industry/Entity Type
Chiropractic
Contact Information for Business Card
Dr. Bram Holtvick, D.C.
Clinic name - Fernway Chiropractic
2 clinics
location #1
20418 NW Marwick Road
Suite B
North Plains, OR 97133
Location #2
13529 SE Calloway Street
Portland OR 97236
Main phone line 971.555.0143
website : www.FernwayClinics.example
Tag line "Who would you be without pain?"
Colors
Designer to choose colors to be used in the design.
Requirements
Must have
- Use the logo colors -- Want the orange color to be a TRUE orange.
- Both clinic address
- phone number
- website
- personal email - b.holtvick@ReliefBeginsHere.example
- tag line - "Who would you be without pain?"

```html
<!DOCTYPE html>
<html lang="en">
<head>
<meta charset="utf-8">
<title>Fernway Chiropractic – Business Card</title>
<link href="https://fonts.googleapis.com/css2?family=Roboto:ital,wght@0,400;0,500;1,400&family=Roboto+Condensed:wght@700&display=swap" rel="stylesheet">
<style>
  :root {
    --backdrop: #3a3a3c;
    --card: #1e1e20;
    --card-back: #232325;
    --orange: #ff8c00;
    --white: #f2f2f2;
    --muted: #a8a8aa;
    --emboss: #3e3e41;
    --mark: #b9b9bb;
  }
  * { box-sizing: border-box; margin: 0; padding: 0; }
  html, body { width: 799px; height: 1200px; overflow: hidden; }
  body {
    background: var(--backdrop);
    font-family: "Roboto", sans-serif;
    position: relative;
  }
  .card {
    position: absolute;
    left: 80px;
    width: 640px;
    height: 366px;
    border-radius: 4px;
    box-shadow: 0 14px 30px rgba(0,0,0,.45);
    overflow: hidden;
  }
  .card--front { top: 117px; background: var(--card); }
  .card--back { top: 717px; background: var(--card-back); }

  .brand-name {
    position: absolute;
    font-family: "Roboto", sans-serif;
    font-weight: 500;
    text-align: center;
    line-height: 1.15;
    letter-spacing: 6px;
  }
  .brand-name small {
    display: block;
    font-size: 15px;
    letter-spacing: 5px;
  }
  .card--front .brand-name {
    left: 0; right: 0; top: 92px;
    color: var(--emboss);
    font-size: 40px;
  }

  .clinics {
    position: absolute;
    left: 30px; bottom: 70px;
    font-size: 15.5px;
    line-height: 1.6;
    color: var(--white);
  }
  .clinics .label { color: var(--orange); }
  .clinics li { list-style: none; }

  .doctor { position: absolute; left: 34px; top: 40px; }
  .doctor-name {
    font-family: "Roboto Condensed", sans-serif;
    font-weight: 700;
    font-size: 20px;
    color: var(--orange);
  }
  .doctor-title { font-size: 13px; color: var(--muted); margin-top: 3px; }

  .contacts {
    position: absolute; left: 34px; bottom: 46px;
    list-style: none;
    font-size: 14px;
    color: var(--white);
  }
  .contacts li { display: flex; align-items: center; gap: 12px; margin-top: 6px; }
  .contacts svg { width: 12px; height: 12px; fill: var(--orange); flex: none; }

  .card--back .brand-name {
    right: 40px; top: 150px; width: 300px;
    color: var(--mark);
    font-size: 34px;
  }
  .tagline {
    position: absolute;
    right: 40px; top: 232px; width: 300px;
    text-align: center;
    font-style: italic;
    font-size: 14px;
    color: var(--orange);
  }
</style>
</head>
<body>
  <section class="card card--front" aria-label="Card front">
    <div class="brand-name">FERNWAY<small>CHIROPRACTIC</small></div>
    <ul class="clinics">
      <li><span class="label">OUR CLINIC#1:</span> 20418 NW Marwick Road Suite B North Plains, OR 97133</li>
      <li><span class="label">OUR CLINIC#2:</span> 13529 SE Calloway Street Portland OR 97236</li>
    </ul>
  </section>

  <section class="card card--back" aria-label="Card back">
    <div class="doctor">
      <p class="doctor-name">Dr. Bram Holtvick, D.C.</p>
      <p class="doctor-title">Chiropractic Doctor</p>
    </div>
    <ul class="contacts">
      <li><svg viewBox="0 0 12 12" aria-hidden="true"><path d="M2 1h3l1 3-1.5 1a7 7 0 0 0 2.5 2.5L8 6l3 1v3c0 .6-.4 1-1 1A9 9 0 0 1 1 2c0-.6.4-1 1-1z"/></svg>971.555.0143</li>
      <li><svg viewBox="0 0 12 12" aria-hidden="true"><circle cx="6" cy="6" r="5.5"/><path d="M1 6h10M6 .5v11" stroke="#232325" stroke-width="1"/></svg>www.FernwayClinics.example</li>
      <li><svg viewBox="0 0 12 12" aria-hidden="true"><path d="M0 2h12v8H0z M0 2l6 4 6-4" stroke="#232325" stroke-width="1"/></svg>b.holtvick@ReliefBeginsHere.example</li>
    </ul>
    <div class="brand-name">FERNWAY<small>CHIROPRACTIC</small></div>
    <p class="tagline">Who would you be without pain?</p>
  </section>
</body>
</html>
```